Nectarine Point of Sale Cards for Grocery Retail Markets

We are looking to update our Nectarine point of sale card and price card. The cards will need to be 7" x 11" with a .125 bleed - one sided. See attached for the old versions. We would like this to use photos that look like true Washington State Peaches. Here are the bullet points we would like to use: - New Crop!- Tree Ripened- Excellent FlavorNOTE: The price card just needs to have a space where a retailer can write in the sale price of the item. See attachment with the white box.

Target Market(s)

Retail market shoppers

Requirements
Must have
• Pictures of Nectarines Only

```html
<!DOCTYPE html>
<html lang="en">
<head>
<meta charset="utf-8">
<title>Nectarine Point of Sale Card</title>
<link rel="stylesheet" href="https://fonts.googleapis.com/css2?family=Parisienne&family=Roboto:wght@300;400;700&display=swap">
<style>
  :root {
    --page-bg: #eeeeee;
    --card-white: #ffffff;
    --brand-green: #3f9637;
    --ring-white: #ffffff;
    --muted-grey: #a3a3a3;
    --peach-orange: #f39a3c;
    --peach-red: #d8432a;
    --peach-yellow: #f7c25a;
  }
  * { margin: 0; padding: 0; box-sizing: border-box; }
  html, body {
    width: 689px;
    height: 1200px;
    overflow: hidden;
    background: var(--page-bg);
  }
  .pos-card {
    position: absolute;
    left: 34px;
    top: 402px;
    width: 620px;
    height: 395px;
    background: var(--card-white);
    overflow: hidden;
  }
  .produce-photo {
    position: absolute;
    left: 0;
    top: 0;
    width: 620px;
    height: 302px;
    background:
      radial-gradient(circle at 8% 30%, var(--peach-yellow) 0, transparent 22%),
      radial-gradient(circle at 20% 75%, var(--peach-red) 0, transparent 25%),
      radial-gradient(circle at 88% 25%, var(--peach-orange) 0, transparent 28%),
      radial-gradient(circle at 80% 80%, var(--peach-yellow) 0, transparent 25%),
      linear-gradient(135deg, #e8602f 0%, #f39a3c 50%, #f2ad4a 100%);
  }
  .headline-seal {
    position: absolute;
    left: 0;
    top: 0;
    width: 620px;
    height: 302px;
  }
  .seal-script { font-family: "Parisienne", cursive; font-size: 34px; fill: var(--ring-white); }
  .seal-point { font-family: "Roboto", sans-serif; font-weight: 700; font-size: 23px; fill: var(--ring-white); }
  .seal-region { font-family: "Roboto", sans-serif; font-weight: 300; font-size: 21px; fill: var(--ring-white); letter-spacing: 0.5px; }
  .seal-product { font-family: "Roboto", sans-serif; font-weight: 700; font-size: 22px; fill: var(--ring-white); }
  .price-band {
    position: absolute;
    left: 0;
    top: 302px;
    width: 620px;
    height: 93px;
    background: var(--card-white);
  }
  .grower-mark {
    position: absolute;
    left: 18px;
    top: 24px;
    display: flex;
    align-items: center;
    gap: 10px;
  }
  .grower-dot {
    width: 46px;
    height: 46px;
    border-radius: 50%;
    background: var(--brand-green);
  }
  .grower-name {
    font-family: "Roboto", sans-serif;
    font-weight: 700;
    font-size: 14px;
    line-height: 15px;
    color: var(--brand-green);
  }
  .sale-price-space {
    position: absolute;
    left: 238px;
    top: 36px;
    font-family: "Roboto", sans-serif;
    font-weight: 400;
    font-size: 18px;
    color: var(--muted-grey);
  }
  .nectarine-cluster {
    position: absolute;
    left: 470px;
    top: 282px;
    width: 138px;
    height: 104px;
    border-radius: 50% 50% 45% 45%;
    background: radial-gradient(circle at 45% 45%, #f6e6c8 0, #e0402f 35%, #b5202a 75%, #3c8a2c 100%);
  }
</style>
</head>
<body>
  <div class="pos-card">
    <div class="produce-photo" role="img" aria-label="Photo of a pile of ripe red and orange nectarines filling the card"></div>
    <svg class="headline-seal" viewBox="0 0 620 302" aria-label="Taste The Difference. New Crop! Tree Ripened. Excellent Flavor. Washington State Peaches">
      <circle cx="318" cy="150" r="170" fill="var(--brand-green)"/>
      <circle cx="318" cy="150" r="161" fill="none" stroke="var(--ring-white)" stroke-width="1"/>
      <text class="seal-script" x="318" y="76" text-anchor="middle">Taste The Difference</text>
      <text class="seal-point" x="318" y="122" text-anchor="middle">New Crop!</text>
      <text class="seal-point" x="318" y="157" text-anchor="middle">Tree Ripened</text>
      <text class="seal-point" x="318" y="192" text-anchor="middle">Excellent Flavor</text>
      <line x1="197" y1="215" x2="439" y2="215" stroke="var(--ring-white)" stroke-width="0.8" opacity="0.8"/>
      <text class="seal-region" x="318" y="246" text-anchor="middle">WASHINGTON</text>
      <text class="seal-product" x="318" y="273" text-anchor="middle">STATE PEACHES</text>
    </svg>
    <div class="price-band">
      <div class="grower-mark">
        <span class="grower-dot"></span>
        <span class="grower-name">Cascade Orchard<br>Growers</span>
      </div>
      <div class="sale-price-space">Sale Price Space</div>
    </div>
    <div class="nectarine-cluster" role="img" aria-label="Illustration of whole and halved nectarines with green leaves"></div>
  </div>
</body>
</html>
```